Redesign of dating app main page

Task is redesign of main page of dating app. Page design is attached. UX design should be the same (buttons of the top of screen , scrolling down). Searching users profiles with their buttons should be more divided.

```html
<!DOCTYPE html>
<html lang="en">
<head>
<meta charset="utf-8">
<title>Dating App – Discover</title>
<link href="https://fonts.googleapis.com/css2?family=Open+Sans:wght@400;600;700&display=swap" rel="stylesheet">
<style>
  :root {
    --stage: #1b1c26;
    --screen: #ffffff;
    --ink: #2b2b2b;
    --ink-soft: #6a6a6a;
    --icon: #b9b9bd;
    --accent: #e23a52;
    --photo-a: #4f6a3e;
    --photo-b: #b9a98a;
    --photo-c: #d9cdb6;
    --next-a: #c9c2b4;
    --next-b: #9c8f7c;
  }
  * { margin: 0; padding: 0; box-sizing: border-box; }
  html, body { width: 1127px; height: 1200px; overflow: hidden; }
  body {
    background: var(--stage);
    font-family: "Open Sans", Arial, sans-serif;
    position: relative;
  }
  .app-screen {
    position: absolute;
    left: 263px; top: 118px;
    width: 600px; height: 963px;
    background: var(--screen);
    overflow: hidden;
  }
  .status-bar {
    height: 27px;
    display: flex; align-items: center; justify-content: space-between;
    padding: 0 22px;
    font-size: 12px; font-weight: 600; color: var(--ink);
  }
  .status-left { display: flex; align-items: center; gap: 8px; }
  .signal { display: flex; gap: 2px; }
  .signal span { width: 6px; height: 6px; border-radius: 50%; background: var(--ink); }
  .signal span.off { background: none; border: 1px solid var(--ink); }
  .status-right { display: flex; align-items: center; gap: 10px; }
  .top-nav {
    height: 77px;
    display: flex; align-items: center; justify-content: space-between;
    padding: 0 26px;
  }
  .top-nav svg { width: 38px; height: 38px; fill: var(--icon); }
  .profile-card { margin: 0 31px; }
  .profile-photo {
    position: relative;
    height: 614px;
    background: linear-gradient(135deg, var(--photo-a) 0%, var(--photo-b) 55%, var(--photo-c) 100%);
  }
  .photo-dots {
    position: absolute; bottom: 22px; left: 50%; transform: translateX(-50%);
    display: flex; gap: 5px;
  }
  .photo-dots span { width: 8px; height: 8px; border-radius: 50%; border: 1.5px solid #fff; }
  .photo-dots span.active { background: #fff; }
  .distance {
    position: absolute; right: 22px; bottom: 16px;
    display: flex; align-items: center; gap: 4px;
    color: #fff; font-size: 15px; font-weight: 600;
  }
  .distance svg { width: 14px; height: 16px; fill: #fff; }
  .profile-info {
    height: 109px;
    display: flex; align-items: center; justify-content: space-between;
    padding: 0 22px;
  }
  .profile-name { font-size: 30px; font-weight: 600; color: var(--ink); line-height: 1; }
  .profile-name .age { font-size: 21px; font-weight: 400; color: var(--ink-soft); }
  .profile-job { font-size: 15px; color: var(--ink-soft); margin-top: 4px; }
  .dismiss-button {
    width: 46px; height: 46px; border-radius: 50%;
    border: 2.5px solid var(--accent);
    display: flex; align-items: center; justify-content: center;
    margin-left: 80px;
  }
  .dismiss-button svg { width: 18px; height: 18px; stroke: var(--accent); stroke-width: 3; stroke-linecap: round; }
  .request-button {
    background: var(--accent); color: #fff;
    font-size: 16px; font-weight: 600;
    padding: 9px 18px; border-radius: 22px;
    margin-left: auto;
  }
  .next-card {
    margin: 15px 31px 0;
    height: 140px;
    background: linear-gradient(90deg, var(--next-a), var(--next-b) 50%, var(--next-a));
  }
</style>
</head>
<body>
  <main class="app-screen">
    <div class="status-bar">
      <div class="status-left">
        <div class="signal"><span></span><span></span><span></span><span></span><span class="off"></span></div>
        <span>4:34 PM</span>
      </div>
      <div class="status-right">
        <svg width="18" height="13" viewBox="0 0 18 13"><path d="M9 13l3-3.5a4.5 4.5 0 0 0-6 0zM2 5.5a10 10 0 0 1 14 0l-1.6 1.8a7.6 7.6 0 0 0-10.8 0zM0 2.8a13 13 0 0 1 18 0l-1.4 1.5a11 11 0 0 0-15.2 0z" fill="#2b2b2b"/></svg>
        <svg width="30" height="13" viewBox="0 0 30 13"><rect x="0.5" y="0.5" width="26" height="12" rx="2" fill="none" stroke="#2b2b2b"/><rect x="2" y="2" width="20" height="9" fill="#2b2b2b"/><rect x="27.5" y="4" width="2" height="5" fill="#2b2b2b"/></svg>
      </div>
    </div>

    <nav class="top-nav">
      <svg viewBox="0 0 24 24" aria-label="Profile"><circle cx="12" cy="7.5" r="5"/><path d="M2 23c0-6 4.5-9 10-9s10 3 10 9z"/></svg>
      <svg viewBox="0 0 24 24" aria-label="Matches"><path d="M12 22s-10-6.5-10-13.2A5.6 5.6 0 0 1 12 5.3a5.6 5.6 0 0 1 10 3.5C22 15.5 12 22 12 22z"/></svg>
      <svg viewBox="0 0 24 24" aria-label="Messages"><path d="M3 4h13a2 2 0 0 1 2 2v7a2 2 0 0 1-2 2H9l-4 3v-3H3a2 2 0 0 1-2-2V6a2 2 0 0 1 2-2zm17 4h1a2 2 0 0 1 2 2v7a2 2 0 0 1-2 2h-1v3l-4-3h-5l1.5-2H18a2 2 0 0 0 2-2z"/><circle cx="5" cy="9.5" r="1.2" fill="#fff"/><circle cx="9.5" cy="9.5" r="1.2" fill="#fff"/><circle cx="14" cy="9.5" r="1.2" fill="#fff"/></svg>
    </nav>

    <article class="profile-card">
      <div class="profile-photo" role="img" aria-label="Profile photo of a woman in a sun hat and sunglasses outdoors">
        <div class="photo-dots"><span></span><span class="active"></span><span></span><span></span><span></span></div>
        <div class="distance">
          <svg viewBox="0 0 12 16"><path d="M6 0a6 6 0 0 1 6 6c0 4.5-6 10-6 10S0 10.5 0 6a6 6 0 0 1 6-6zm0 3.5A2.5 2.5 0 1 0 6 8.5 2.5 2.5 0 0 0 6 3.5z"/></svg>
          9km
        </div>
      </div>
      <div class="profile-info">
        <div>
          <div class="profile-name">Mira <span class="age">25</span></div>
          <div class="profile-job">Developer</div>
        </div>
        <div class="dismiss-button" aria-label="Dismiss">
          <svg viewBox="0 0 18 18"><path d="M3 3l12 12M15 3L3 15"/></svg>
        </div>
        <div class="request-button">Send Request</div>
      </div>
    </article>

    <div class="next-card" role="img" aria-label="Next profile photo, partly visible"></div>
  </main>
</body>
</html>
```